Elegant, Playful ReDesign of Paperlark Website in wordpress - Budget has been raised

Project Brief: Paperlark Website Redesign in WordPress

Introduction: Paperlark, a cutting-edge document creation solution, aims to revolutionize the tedious process of crafting contracts, offers, forms, and other documents. By saving customers valuable time, streamlining workflows, and minimizing human error, Paperlark has become an essential tool. As a technology company with a diverse clientele, we're set to boost our online presence through a refreshed WordPress website. Beyond a modernized website, we aspire to establish a stronger brand identity, incorporating graphic elements seamlessly into our online presence.

Current Status: Currently hosted on WordPress, Paperlark's existing website serves its purpose but is ready for a visual transformation. Our goal is to maintain a modern and attractive appearance while upholding our commitment to simplicity and efficiency. Notably, the website is currently only in Danish. The redesigned structure should include a language switch function to cater to future international customers.

Objectives:
• Modern Aesthetic: Redesign the website with a fresh and modern vibe, reflecting innovation in the document creation sphere.
• User-Friendly: Prioritize an intuitive design for seamless navigation, ensuring visitors easily understand our offerings and benefits.
• Informative Content: Strike a balance between attractiveness and informativeness, clearly communicating Paperlark's value proposition and simplifying business processes.
• Graphic Elements: Integrate visually appealing graphics that enhance the site's aesthetics and contribute to our overall visual identity. These elements should be versatile for future use in social media, advertisements, and other branding materials.
• Brand Recognition: Maintain our current logo and color scheme while exploring creative ways to establish a distinctive brand identity. The website should be a cornerstone for a cohesive branding strategy.
• Media Integration: Include images or videos on the website to enhance engagement. Find suitable, free-to-use visuals.
• Responsiveness: Ensure the design is responsive and works seamlessly on all devices.
• Demo Booking Form: Improve the design of the form to book a demo.
• Multilingual Support: Enable language transformation; the website is currently in Danish but should cater to other countries.

Guidelines:
• Typography: Up to the designer's discretion.
• Images/Videos: Must be free to use without additional charges.
• WordPress Theme: Use any WordPress theme below $100.
• Logo Redesign: Not needed; stick to the referenced color palette, as our new logo uses these colors.
• Color Palette: Stick to the existing company colors for consistency:
RGB
• #000b3c
• #004c6c
• #319ac3
• Greytones and white are also allowed
• Creativity Encouraged: Embrace creativity within the color palette for the layout, visuals, and overall user experience.

Conclusion: The Paperlark website redesign marks an exciting opportunity to enhance our online presence. Our goal is to achieve a balance between a modern, attractive design and a clear, informative representation of our innovative solutions. We envision the revamped website as the foundation for a compelling online brand presence, with versatile graphic elements resonating across various digital platforms.

Sections that the website must include: Space for customer logos, space for testimonials, Space and redesign for display of price structure and price comparison, sections for company details and other information.

Design should also include a redesign of the customer cases section.
Generally there should just be a redesign of all things that are on the website.

Link to current website: https://paperlark-example.com/

+50 employees.

Document automation

Coded - Design and coding required

5+ page

0054AA
0677BA
7BADD7
CADEEF
E8F1F8

• The new webpage must have the same pages as the current one. Frontpage, Book demo, About us, Case stories and Pricing

```html
<!DOCTYPE html>
<html lang="da">
<head>
<meta charset="utf-8">
<title>Paperlark – Opret fejlfrie kontrakter og tilbud hurtigt</title>
<link href="https://fonts.googleapis.com/css2?family=Montserrat:wght@400;500;600;700;800&display=swap" rel="stylesheet">
<style>
:root{
  --navy:#000b3c;
  --deep:#004c6c;
  --sky:#319ac3;
  --blue:#0677ba;
  --royal:#0054aa;
  --pale:#e8f1f8;
  --grey-bg:#f2f2f2;
  --text:#222;
  --muted:#555;
  --line:#d6dde2;
  --green:#3fb86a;
  --footer:#1c1c1c;
}
*{box-sizing:border-box;margin:0;padding:0}
html,body{width:1200px;height:5391px;overflow:hidden}
body{position:relative;font-family:'Montserrat',sans-serif;color:var(--text);background:#fff}
.abs{position:absolute}
section,header,footer{position:absolute;left:0;width:1200px}
.h2{font-weight:700;font-size:24px;text-align:center;color:var(--navy);letter-spacing:.3px}
.h2::after{content:"";display:block;width:56px;height:3px;background:var(--sky);margin:14px auto 0}
.btn{display:inline-block;border-radius:20px;font-weight:700;font-size:13px;text-transform:uppercase;letter-spacing:.3px;text-align:center}
.btn-dark{background:var(--navy);color:#fff;padding:9px 20px}
.btn-blue{background:var(--blue);color:#fff}
/* header */
.topbar{position:absolute;left:418px;top:0;width:782px;height:38px;background:var(--blue);border-bottom-left-radius:22px;color:#fff;font-size:12px}
.topbar span{position:absolute;top:12px;white-space:nowrap}
.ico{display:inline-block;width:20px;height:20px;border-radius:50%;background:rgba(255,255,255,.25);vertical-align:middle;margin-right:8px;margin-top:-4px}
.logo{position:absolute;left:125px;top:32px;display:flex;align-items:center;gap:10px;font-weight:800;font-size:28px;color:var(--navy)}
.logo i{display:block;width:40px;height:40px;background:var(--deep)}
.nav{position:absolute;top:67px;font-size:13px;color:#333}
.nav a{position:absolute;white-space:nowrap}
/* hero */
.hero{top:109px;height:581px;background:linear-gradient(100deg,var(--deep) 0%,var(--royal) 45%,var(--blue) 100%);overflow:hidden}
.hero h1{position:absolute;left:105px;top:104px;color:#fff;font-weight:800;font-size:42px;line-height:50px;letter-spacing:.5px}
.checks{position:absolute;left:105px;top:270px;list-style:none;color:#fff;font-size:14px}
.checks li{height:30px;display:flex;align-items:center;gap:10px}
.tick{width:15px;height:15px;border-radius:50%;background:var(--green);display:inline-block;position:relative}
.tick::after{content:"";position:absolute;left:5px;top:2px;width:4px;height:7px;border:solid #fff;border-width:0 2px 2px 0;transform:rotate(45deg)}
.hero-cta{position:absolute;left:105px;top:400px;border:2px solid #fff;color:#fff;padding:6px 14px;border-radius:14px;font-size:12px;font-weight:700}
.hero-art{position:absolute;left:560px;top:60px;width:560px;height:400px;border-radius:30px;background:radial-gradient(ellipse at 60% 50%,rgba(123,173,215,.55),rgba(6,119,186,0) 70%)}
.dots{position:absolute;display:flex;gap:6px}
.dots b{width:8px;height:8px;border-radius:50%;background:#fff;opacity:.6}
.dots b.on{opacity:1;background:var(--sky)}
/* why */
.why h2{position:absolute;top:788px;width:1200px}
.card{position:absolute;top:884px;height:284px;border:1px solid #e3e3e3;border-radius:6px;background:#fff;text-align:center;padding:0 30px;box-shadow:0 2px 8px rgba(0,0,0,.05)}
.card .ci{width:92px;height:92px;margin:36px auto 22px;border-radius:50%;background:linear-gradient(135deg,var(--sky),var(--navy));display:flex;align-items:center;justify-content:center}
.card h3{font-size:19px;font-weight:700;color:var(--navy);margin-bottom:14px}
.card p{font-size:12.5px;line-height:19px;color:var(--muted)}
.card.feat{background:linear-gradient(135deg,var(--deep),var(--blue));border:none}
.card.feat h3,.card.feat p{color:#fff}
.card.feat .ci{background:#fff}
/* mobile */
.mobile{top:1250px;height:373px;background:var(--grey-bg)}
.mobile-art{position:absolute;left:125px;top:25px;width:388px;height:320px;border-radius:50%;background:radial-gradient(circle at 45% 50%,#fff 0 42%,#dcdcdc 43% 70%,transparent 71%)}
.mobile h2{position:absolute;left:611px;top:73px;font-size:22px;font-weight:700;color:var(--navy)}
.mobile h2::after{content:"";display:block;width:56px;height:3px;background:var(--sky);margin-top:12px}
.mobile p{position:absolute;left:611px;top:130px;width:490px;font-size:14px;line-height:24px;color:#333}
/* logos */
.logos h2{position:absolute;top:1736px;width:1200px}
.lgrid{position:absolute;left:105px;top:1826px;width:990px;height:264px}
.cell{position:absolute;width:247px;height:88px;background:#eef2f3;border:1px solid #dfe5e7;display:flex;align-items:center;justify-content:center;font-size:20px;font-weight:700;color:#5a5a5a}
.cell.hi{background:#fff;box-shadow:0 4px 14px rgba(0,0,0,.12);z-index:2;color:#333}
/* pricing */
.pricing{top:2171px;height:976px;background:linear-gradient(160deg,var(--navy) 0%,var(--deep) 40%,var(--blue) 80%,var(--sky) 100%);color:#fff}
.pricing h2{position:absolute;top:112px;width:1200px;text-align:center;font-size:24px;font-weight:700}
.pricing .lead{position:absolute;left:100px;top:166px;width:1000px;text-align:center;font-size:15px;line-height:23px}
.toggle{position:absolute;left:438px;top:231px;display:flex;background:#fff;border-radius:18px;padding:3px;z-index:3}
.toggle span{padding:6px 16px;font-size:13px;font-weight:700;color:var(--navy);border-radius:16px;white-space:nowrap}
.toggle span.on{background:var(--pale);color:var(--blue)}
.plan{position:absolute;background:#fff;color:#333;padding:28px 32px}
.plan .pi{width:20px;height:18px;background:var(--navy);border-radius:3px;margin-bottom:10px}
.plan h3{font-size:15px;font-weight:700;color:var(--sky);margin-bottom:8px}
.plan .save{display:inline-block;background:var(--navy);color:#fff;font-size:9px;font-weight:700;padding:5px 12px;border-radius:12px}
.plan .price{font-size:26px;font-weight:800;color:var(--blue);margin:10px 0 4px}
.plan .per{font-size:10px;margin-bottom:12px}
.plan ul{list-style:none;font-size:10.5px;line-height:20px}
.plan li::before{content:"";display:inline-block;width:9px;height:9px;border-radius:50%;background:var(--navy);margin-right:6px;vertical-align:-1px}
.plan .btn{margin-top:14px;font-size:11px;padding:7px 16px}
.plan.pro{background:var(--blue);color:#fff;padding-top:26px}
.plan.pro h3{color:#fff}
.plan.pro .price{color:#fff;font-size:30px}
.plan.pro li::before{background:#fff}
.plan.pro .btn{border:2px solid #fff;background:transparent;color:#fff}
/* features */
.features h2{position:absolute;top:3223px;width:1200px}
.flist{position:absolute;top:3333px;list-style:none;font-size:15px;color:#222}
.flist li{height:33px;display:flex;align-items:center;gap:4px;white-space:nowrap}
.flist li::before{content:"";width:12px;height:12px;border-radius:50%;background:var(--sky);display:inline-block}
.video{position:absolute;left:649px;top:3287px;width:450px;height:336px;border-radius:50%;background:radial-gradient(ellipse at 55% 50%,#2d3a42 0 38%,#e9e9e9 39% 68%,transparent 69%)}
/* testimonials */
.testi{top:3713px;height:622px;background:#f3f4f5}
.testi h2{position:absolute;top:125px;width:1200px}
.tcard{position:absolute;top:192px;height:268px;background:#fff;border-radius:4px}
.photo{position:absolute;width:90px;height:120px;border-radius:6px;background:linear-gradient(180deg,#c9d3da,#7a8b97)}
.tname{position:absolute;font-size:11px;font-weight:700;text-align:center;color:#222;line-height:15px}
.trole{display:block;font-weight:500;font-size:8px;color:var(--sky)}
.quote{position:absolute;font-size:12.5px;line-height:19px;color:#333;border-left:1px solid #ccc;padding-left:18px}
.qm{color:var(--sky);font-weight:800;font-size:22px;line-height:12px;display:block}
.qe{color:var(--sky);font-weight:800;font-size:22px;text-align:right;display:block}
/* demo form */
.demo h2{position:absolute;top:4415px;width:1200px}
.field{position:absolute;border:1px solid #c9c9c9;font-size:13px;color:#333;padding:14px 16px}
.send{position:absolute;left:540px;top:4776px;width:122px;height:30px;line-height:30px;padding:0;border-radius:4px}
/* footer */
.footer-wave{position:absolute;left:0;top:4920px}
.footer{top:5025px;height:366px;background:var(--footer);color:#ddd;font-size:13px}
.fcol{position:absolute;top:40px}
.fcol h4{font-size:20px;font-weight:600;color:#fff;margin-bottom:18px}
.fcol p{line-height:26px}
.flogo{font-weight:800;font-size:28px;color:#fff;display:flex;align-items:center;gap:10px}
.flogo i{width:36px;height:36px;background:#fff;display:block}
.copy{position:absolute;top:325px;width:1200px;text-align:center;font-size:11px;color:#ccc}
.copy b{color:var(--sky);font-weight:500}
</style>
</head>
<body>

<header>
  <div class="topbar">
    <span style="left:76px"><i class="ico"></i>Havnevej 14, 2800 Lyngby</span>
    <span style="left:353px"><i class="ico"></i>contact@paperlark-example.com</span>
    <span style="left:592px"><i class="ico"></i>⌄ Danish</span>
  </div>
  <div class="logo"><i></i>Paperlark</div>
  <nav class="nav">
    <a style="left:485px">Forside</a>
    <a style="left:560px">Kundecases</a>
    <a style="left:667px">Video</a>
    <a style="left:730px">Live demo</a>
    <a style="left:827px">Priser</a>
    <a style="left:891px">Om os</a>
  </nav>
  <a class="btn btn-dark abs" style="left:969px;top:58px;font-size:12px">Book demo</a>
</header>

<section class="hero">
  <div class="hero-art" role="img" aria-label="Illustration af forretningsmand der underskriver et digitalt dokument foran søjlediagrammer"></div>
  <h1>OPRET FEJLFRIE<br>KONTRAKTER OG<br>TILBUD HURTIGT</h1>
  <ul class="checks">
    <li><i class="tick"></i>Få priser beregnet automatisk</li>
    <li><i class="tick"></i>Fjern manuelt arbejde</li>
    <li><i class="tick"></i>Få afsnit indsat automatisk</li>
    <li><i class="tick"></i>Underskriv digitalt</li>
  </ul>
  <a class="hero-cta">KOM I GANG</a>
  <svg class="abs" style="left:0;top:440px" width="1200" height="141" viewBox="0 0 1200 141" preserveAspectRatio="none">
    <path d="M0 40 C300 130 700 150 1200 60 L1200 141 L0 141Z" fill="#7badd7" opacity=".6"/>
    <path d="M0 70 C320 150 760 150 1200 100 L1200 141 L0 141Z" fill="#fff"/>
  </svg>
  <div class="dots" style="left:576px;top:538px"><b class="on"></b><b></b><b></b></div>
</section>

<section class="why">
  <h2 class="h2">HVORFOR VÆLGE OS</h2>
  <div class="card" style="left:132px;width:280px">
    <div class="ci"><svg width="34" height="40" viewBox="0 0 34 40"><path d="M4 2h26M4 38h26M7 2c0 12 20 12 20 18S7 26 7 38M27 2c0 12-20 12-20 18s20 6 20 18" stroke="#fff" stroke-width="3" fill="none"/></svg></div>
    <h3>Spar Tid</h3>
    <p>Reducér dit tidsforbrug med helt op til 90 %, når du opretter kundekontrakter og tilbud .</p>
  </div>
  <div class="card feat" style="left:461px;width:278px">
    <div class="ci"><svg width="36" height="42" viewBox="0 0 36 42"><rect x="4" y="2" width="26" height="36" rx="2" fill="#004c6c"/><path d="M10 12h14M10 19h14M10 26h10" stroke="#fff" stroke-width="2.5"/></svg></div>
    <h3>Høj Kvalitet</h3>
    <p>Automatisering giver dig minimalt arbejde og fjerner fejl i dine dokumenter.</p>
  </div>
  <div class="card" style="left:785px;width:283px">
    <div class="ci"><svg width="44" height="40" viewBox="0 0 44 40"><rect x="3" y="3" width="14" height="12" rx="3" stroke="#fff" stroke-width="3" fill="none"/><rect x="27" y="25" width="14" height="12" rx="3" stroke="#fff" stroke-width="3" fill="none"/><path d="M17 9h14a5 5 0 0 1 0 10H13a5 5 0 0 0 0 10h14" stroke="#fff" stroke-width="3" fill="none"/></svg></div>
    <h3>Strømlinet Flow</h3>
    <p>Bliv guidet hele vejen igennem dokumentet og bed om gennemgang, inden du sender dokumentet til digital signatur.</p>
  </div>
</section>

<section class="mobile">
  <div class="mobile-art" role="img" aria-label="Tablet og mobiltelefon der viser appens dokumentoversigt"></div>
  <h2>AKTIVÉR DIN MOBIL</h2>
  <p>Opret dine dokumenter, når det passer dig. De kan oprettes på hvilken som helst enhed og underskrives langt hurtigere.Opret eksempelvis et tilbud på en mobil eller en tablet, imens du taler med en potentiel kunde til et møde. Få accept det samme, og send den til digital signatur, før du tager hjem.</p>
  <a class="btn btn-blue abs" style="left:611px;top:262px;padding:7px 16px;font-size:12px;background:var(--deep)">KOM I GANG</a>
</section>

<section class="logos">
  <h2 class="h2">KUNDE LOGO</h2>
  <div class="lgrid">
    <div class="cell" style="left:0;top:0;font-size:16px">Stratify Lane</div>
    <div class="cell" style="left:248px;top:0;font-size:17px">Fokal Advokater</div>
    <div class="cell" style="left:496px;top:0;font-size:18px">Brook Packaging</div>
    <div class="cell" style="left:744px;top:0">Webnook</div>
    <div class="cell" style="left:0;top:88px;font-size:14px">Tindra Documents</div>
    <div class="cell hi" style="left:248px;top:88px;font-size:24px">Velora</div>
    <div class="cell" style="left:496px;top:88px;font-size:17px">Kvist Advokatfirma</div>
    <div class="cell" style="left:744px;top:88px">MaxDesk</div>
    <div class="cell" style="left:248px;top:176px;font-size:16px">Lys Advokater</div>
    <div class="cell" style="left:496px;top:176px">Holmsted</div>
  </div>
</section>

<section class="pricing">
  <h2>PRISER</h2>
  <p class="lead">Vælg imellem tre forskellige standard modeller i forhold til hvor mange kontrakter du ønsker automatiseret. Kontakt os hvis du har flere end fem kontrakter, så skræddersyr vi en Enterprise model, der er tilpasset dine behov.</p>
  <div class="toggle"><span>Betaling Månedligt</span><span class="on">Betaling årligt</span></div>

  <div class="plan" style="left:147px;top:359px;width:286px;height:374px">
    <div class="pi"></div>
    <h3>STARTER</h3>
    <span class="save">SPAR 165 KR.</span>
    <div class="price">795 kr.</div>
    <div class="per">pr. måned &nbsp; 250 dokumenter / år</div>
    <ul><li>1 kontraktskabelon</li><li>1 bruger</li><li>+95 kr. per ekstra bruger</li><li>Eksporter til DOCX</li><li>Eksporter til Pdf</li><li>Eget design</li></ul>
    <a class="btn btn-dark">BOOK DEMO</a>
  </div>

  <div class="plan pro" style="left:433px;top:306px;width:331px;height:541px">
    <div class="pi" style="background:#fff"></div>
    <h3>Pro</h3>
    <span class="save">SPAR 295 KR</span>
    <div class="price">1.595 kr.</div>
    <div class="per">pr. måned &nbsp; 1.000 dokumenter / år</div>
    <ul><li>2 kontraktskabeloner</li><li>1 bruger</li><li>+95 kr. per ekstra bruger</li><li>Eksporter til DOCX</li><li>Eksporter til Pdf</li><li>Eget design</li><li>Digital signatur</li><li>Reviewproces</li><li>Flere sprog</li><li>Produktopslag</li><li>Medarbejderopslag</li><li>Dokumenter i mail</li><li>Integration til CRM</li></ul>
    <a class="btn">BOOK DEMO</a>
  </div>

  <div class="plan" style="left:766px;top:359px;width:291px;height:374px">
    <div class="pi"></div>
    <h3>BUSINESS</h3>
    <span class="save">SPAR 555 KR.</span>
    <div class="price">2.795 kr.</div>
    <div class="per">pr. måned &nbsp; 2.000 dokumenter / år</div>
    <ul><li>1 kontraktskabelon</li><li>1 bruger</li><li>+95 kr. per ekstra bruger</li><li>Eksporter til DOCX</li><li>Eksporter til Pdf</li><li>Eget design</li></ul>
    <a class="btn btn-blue" style="background:var(--blue)">VIEW MORE</a>
  </div>
</section>

<section class="features">
  <h2 class="h2">MASSER AF FEATURES</h2>
  <ul class="flist" style="left:105px">
    <li>Eget design</li><li>Beregning af værdier</li><li>Afsnit indsættes automatisk</li><li>Proces for gennemgang</li><li>Digital signatur</li><li>Dokument designer</li><li>Del med kolleger</li>
  </ul>
  <ul class="flist" style="left:368px">
    <li>Opslag i CVR-registeret</li><li>Globalt adresse-register</li><li>Download som DOCX</li><li>Download som Pdf</li><li>Data i regneark</li><li>Integration til CRM</li><li>Integration til sagsstyring</li><li>Flere sprog</li>
  </ul>
  <div class="video" role="img" aria-label="Bærbar computer med introduktionsvideo: Opret tilbud og kontrakter hurtigt og fejlfrit"></div>
</section>

<section class="testi">
  <h2 class="h2">VÆRDSAT OG ANBEFALET AF</h2>
  <div class="tcard" style="left:105px;width:494px">
    <div class="photo" style="left:34px;top:38px" role="img" aria-label="Portræt af kunde"></div>
    <div class="tname" style="left:10px;top:170px;width:140px">Mikkel Aagaard<br>Sørensen<span class="trole">Salgsdirektør – Kvist Advokatfirma</span></div>
    <div class="quote" style="left:178px;top:20px;width:284px"><span class="qm">“</span>eg havde ikke forestillet mig, at vores tilbud bare sådan kunne automatiseres fuldt ud, men vi gav det et skud, fordi jeg så, hvad andre havde gjort med Paperlark. Resultatet er blevet knivskarpt – jeg bliver helt glad når jeg står med et nyt tilbud i hånden.<span class="qe">”</span></div>
  </div>
  <div class="tcard" style="left:628px;width:510px;background:transparent">
    <div class="photo" style="left:40px;top:40px" role="img" aria-label="Portræt af kunde"></div>
    <div class="tname" style="left:8px;top:180px;width:160px">Jonas Brandt Lund<span class="trole">Direktør – Tindra Documents</span></div>
    <div class="quote" style="left:170px;top:20px;width:310px;font-size:12px;line-height:18px"><span class="qm">“</span>Vi havde ledt længe efter den helt rigtige platform til at digitalisere vores unikke paradigmesamling, og var ikke i tvivl efter vi fik demonstreret Paperlark løsning.<br>Det stiller nemlig høje krav til løsningen når komplekse paradigmer skal digitaliseres, og vi ønskede ikke at gå på kompromis med hverken kvalitet eller oplevelsen.<span class="qe">”</span></div>
  </div>
  <div class="dots" style="left:576px;top:514px"><b style="background:#fff;border:1px solid #333;opacity:1"></b><b class="on"></b><b class="on"></b></div>
</section>

<section class="demo">
  <h2 class="h2">BESTILLING AF EN DEMO</h2>
  <div class="field" style="left:205px;top:4483px;width:383px;height:53px">Fornavn*</div>
  <div class="field" style="left:609px;top:4483px;width:384px;height:53px">Efternavn*</div>
  <div class="field" style="left:205px;top:4559px;width:383px;height:52px">Telefonnummer*</div>
  <div class="field" style="left:609px;top:4559px;width:384px;height:52px">E-mail*</div>
  <div class="field" style="left:205px;top:4636px;width:788px;height:113px">Besked*</div>
  <a class="btn btn-dark send">INDSEND</a>
</section>

<svg class="footer-wave" width="1200" height="110" viewBox="0 0 1200 110" preserveAspectRatio="none">
  <path d="M0 70 C400 10 800 0 1200 20 L1200 110 L0 110Z" fill="#0677ba"/>
  <path d="M0 105 C400 40 800 30 1200 55 L1200 110 L0 110Z" fill="#1c1c1c"/>
</svg>
<footer class="footer">
  <div class="fcol" style="left:105px;top:45px">
    <div class="flogo"><i></i>Paperlark</div>
    <p style="margin-top:20px;font-size:11px;line-height:18px">Privatlivspolitik<br>Licens- Og Abonnementsbetingelser</p>
    <div style="width:32px;height:32px;border-radius:50%;background:var(--sky);margin-top:12px"></div>
  </div>
  <div class="fcol" style="left:404px">
    <h4>Hurtige Links</h4>
    <p>Forside<br>Kundecases<br>Video<br>Live demo<br>Priser<br>Om os</p>
  </div>
  <div class="fcol" style="left:609px">
    <h4>Kontakt Os</h4>
    <p>contact@paperlark-example.com<br>+45 31 20 48 56<br>Havnevej 14, 2800 Lyngby</p>
  </div>
  <div class="fcol" style="left:892px;width:220px">
    <h4>Mød Os Online</h4>
    <p style="line-height:23px">Vi vil meget gerne linke og dele tanker og idéer. Følg os og hold dig opdateret på de seneste nyheder.</p>
  </div>
  <div class="copy">©Copyrights 2024 <b>PAPERLARK</b> | Alle rettigheder forbeholdes</div>
</footer>

</body>
</html>
```